Web Design Project For Hot Tub Company [DETAILED instructions inside with a VIDEO!!]

Site will be aimed at individual consumers and not business owners. The purpose of the site is NOT to sell hot tubs online, but to entice people to come to the actual store.

According to the client, it is mostly MEN who initiate contact, while the WOMEN come into the store. This means, the design elements should appeal to MEN more so than to WOMEN.

Right now, the clients only web presence is this Bramble Listings ad:

-LINK-
http://www.bramblelistings-example.net/albuquerque-nm/mip/warm-soaks-albuquerque-381724059
-

Site layout will include an area for a large video on the top, below the menu bar. There will be NO optin form on this site, so there will be some open space next to the video. Be creative and use it to highlight something unique about the business (they pride themselves on their high-end products, low monthly maintenance fees, and after purchase care-the company offers FREE delivery, installation, training, 2 free "drain and fills" and a 30-exchange guarantee.) with an interesting graphic.

Below that, a standard FOUR column layout with images and text that can be hyperlinked later to interior pages. Interior pages will include a sidebar. Below that, a standard footer.

Navigation will include the following: Home, About Us, Models, After Market Service, Testimonials, , and Contact Us.

Ideally, this company's site should appeal to higher income couples without children, new homeowners, and wealthy families.

Company's Logo is attached

Upper middle class to upper class families-boyfriends, husbands and fathers mostly.

Business

• -Area for a video player
-Fun, inviting layout that will appeal to upper middle class husbands and boyfriends.
• *Creativity!!!!

A website with a header, a horizontal navigation bar, a video, a four column layout, and a footer are pretty common and standard. Use your creativity to stay within our parameters without looking like a boring, cookie-cutter website.

Though the site should appeal to men, do not exclude women.
• *An optin form

```html
<!DOCTYPE html>
<html lang="en">
<head>
<meta charset="utf-8">
<title>Warm Soaks Albuquerque</title>
<link rel="stylesheet" href="https://fonts.googleapis.com/css2?family=Arimo:ital,wght@0,400;0,700;1,700&family=Ubuntu:ital,wght@0,300;0,400;0,500;0,700;1,500&display=swap">
<style>
:root{
  --sky-top:#e2f1fb;
  --sky-mid:#c3e2f6;
  --sky-deep:#4a93d6;
  --brand:#1f5fbf;
  --navy:#1b3f8f;
  --nav-top:#3a9ce0;
  --nav-bottom:#1569b3;
  --nav-line:#0f5596;
  --orange-top:#ffb12c;
  --orange-bottom:#f07d00;
  --feature:#1a9ad6;
  --text:#222;
  --cream:#efe3c8;
  --footer-head:#1b66b3;
  --button-top:#6cc2f5;
  --button-bottom:#1e8bd8;
  --page:#f1f2f3;
}
*{box-sizing:border-box;margin:0;padding:0}
html,body{width:813px;height:1200px;overflow:hidden}
body{position:relative;background:var(--page);font-family:"Arimo",Arial,sans-serif;color:var(--text)}
.page-top{position:absolute;left:0;top:0;width:813px;height:566px;
  background:
    radial-gradient(ellipse 160px 120px at 790px 240px,rgba(255,255,255,.75),rgba(255,255,255,0)),
    radial-gradient(ellipse 120px 90px at 770px 400px,rgba(255,255,255,.5),rgba(255,255,255,0)),
    linear-gradient(180deg,var(--sky-top) 0,var(--sky-mid) 165px,#7fbbe9 200px,var(--sky-deep) 400px,#6aa9e0 500px,#eef6fc 566px)}
.page-body{position:absolute;left:0;top:566px;width:813px;height:443px;background:#fff}
.brand{position:absolute;left:36px;top:62px;display:flex;align-items:center;gap:14px}
.brand-mark{width:58px;height:58px;border-radius:50%;background:var(--brand)}
.brand-name{font-family:"Ubuntu",sans-serif;font-weight:700;color:var(--brand);line-height:1}
.brand-name .line1{display:block;font-size:42px}
.brand-name .line2{display:block;font-size:20px;letter-spacing:3px;margin-top:4px}
.social{position:absolute;left:625px;top:17px;display:flex;gap:9px}
.social span{width:24px;height:24px;border-radius:50%;background:#2c5aa8;border:2px solid #fff;box-shadow:0 1px 2px rgba(0,0,0,.3)}
.social span:nth-child(2){background:#1ea9e6}
.social span:nth-child(3){background:#f29b1d}
.social span:nth-child(4){background:#c9362b}
.phone{position:absolute;left:567px;top:119px;display:flex;align-items:center;gap:8px}
.phone-dot{width:28px;height:28px;border-radius:50%;background:#1ea2e6}
.phone-number{font:italic 700 19px "Arimo",sans-serif;color:var(--navy);letter-spacing:1px}
.main-nav{position:absolute;left:23px;top:159px;width:740px;height:36px;border-radius:18px;
  background:linear-gradient(180deg,var(--nav-top),var(--nav-bottom));display:flex;overflow:hidden;
  box-shadow:0 2px 4px rgba(0,0,0,.25);border:1px solid var(--nav-line)}
.main-nav a{display:flex;align-items:center;justify-content:center;color:#fff;text-decoration:none;font:12px "Arimo",sans-serif;
  border-right:1px solid var(--nav-line);box-shadow:inset -1px 0 0 rgba(255,255,255,.25)}
.main-nav a:last-child{border-right:0;box-shadow:none}
.main-nav a.is-current{background:linear-gradient(180deg,var(--orange-top),var(--orange-bottom))}
.hero{position:absolute;left:23px;top:214px;width:740px;height:292px;border:5px solid #fff;border-radius:16px;overflow:hidden;
  box-shadow:0 2px 8px rgba(0,0,0,.3)}
.hero-photo{position:absolute;inset:0;
  background:
    linear-gradient(180deg,rgba(150,190,215,0) 0,rgba(150,190,215,0) 62%,rgba(150,185,205,.75) 78%,rgba(120,160,185,.85) 100%),
    linear-gradient(90deg,#9a9a7c 0,#cfcbc0 14%,#e7e3dc 28%,#d6b29a 44%,#e3d8cf 58%,#caa28c 72%,#dcd6d2 88%,#b9c1c6 100%)}
.hero-play{position:absolute;left:343px;top:118px}
.hero-caption{position:absolute;left:0;bottom:0;width:360px;height:53px;background:rgba(30,30,30,.85);
  clip-path:polygon(0 0,88% 0,100% 100%,0 100%);padding:10px 16px;color:#fff}
.hero-caption h2{font:400 17px "Ubuntu",sans-serif;letter-spacing:.2px}
.hero-caption p{font:700 9px "Arimo",sans-serif;margin-top:3px}
.water{position:absolute;left:0;top:510px}
.features{position:absolute;left:0;top:589px;width:813px;height:140px}
.feature{position:absolute;top:0;width:130px;margin-left:-65px;text-align:center}
.feature-disc{display:block;width:104px;height:104px;margin:0 auto;border-radius:50%;border:4px solid #fff;overflow:hidden;
  box-shadow:0 0 0 1px #cfcfcf,0 2px 5px rgba(0,0,0,.2)}
.feature-disc svg{display:block;width:96px;height:96px}
.feature-label{margin-top:13px;font:700 12.5px/14px "Arimo",sans-serif;color:var(--feature);text-transform:uppercase}
.divider{position:absolute;left:28px;top:746px;width:740px;height:2px;background:linear-gradient(90deg,#fff,#dcdcdc 20%,#dcdcdc 80%,#fff)}
.card{position:absolute;top:766px;width:168px}
.card-photo{position:relative;height:78px;border:1px solid #8a8a8a}
.card-photo span{position:absolute;left:0;bottom:0;background:rgba(20,20,20,.75);color:#fff;font:300 17px "Ubuntu",sans-serif;padding:1px 4px 1px}
.card p{margin-top:13px;font:400 10px/15.5px "Ubuntu",sans-serif;letter-spacing:-.05px}
.more-info{position:absolute;top:180px;left:24px;width:113px;height:23px;border-radius:12px;
  background:linear-gradient(180deg,var(--button-top),var(--button-bottom));color:#fff;text-decoration:none;
  font:italic 700 9.5px/23px "Arimo",sans-serif;text-align:center;box-shadow:0 1px 2px rgba(0,0,0,.3)}
.site-footer{position:absolute;left:0;top:1009px;width:813px;height:142px;background:#fff;box-shadow:0 2px 6px rgba(0,0,0,.15)}
.footer-col{position:absolute;top:0;height:128px;padding-top:22px;font-family:"Ubuntu",sans-serif}
.footer-col+.footer-col{border-left:1px solid #e2e2e2}
.footer-col h3{font:italic 500 10.5px "Ubuntu",sans-serif;color:var(--footer-head);margin-bottom:10px}
.footer-col ul{list-style:none}
.footer-col li{font-size:10px;line-height:18px;padding-left:10px;position:relative}
.footer-col li::before{content:"";position:absolute;left:0;top:8px;width:3px;height:3px;border-radius:50%;background:var(--footer-head)}
.footer-col.contact li{line-height:15px}
.footer-col.contact li::before{top:6px}
.copyright{position:absolute;left:0;top:1163px;width:813px;text-align:center;font:10px "Ubuntu",sans-serif;color:#222}
</style>
</head>
<body>
<div class="page-top"></div>
<div class="page-body"></div>

<header>
  <div class="brand">
    <span class="brand-mark"></span>
    <span class="brand-name"><span class="line1">Warm Soaks</span><span class="line2">ALBUQUERQUE</span></span>
  </div>
  <div class="social" aria-label="Social links"><span></span><span></span><span></span><span></span></div>
  <div class="phone"><span class="phone-dot"></span><span class="phone-number">(505) 555-0182</span></div>
</header>

<nav class="main-nav">
  <a class="is-current" href="#" style="width:102px">HOME</a>
  <a href="#" style="width:105px">ABOUT US</a>
  <a href="#" style="width:95px">MODELS</a>
  <a href="#" style="width:173px">AFTER MARKET SERVICE</a>
  <a href="#" style="width:127px">TESTIMONIALS</a>
  <a href="#" style="width:138px">CONTACT US</a>
</nav>

<section class="hero">
  <div class="hero-photo" role="img" aria-label="Video still: a smiling couple relaxing together in a hot tub"></div>
  <svg class="hero-play" width="46" height="46" viewBox="0 0 46 46" aria-hidden="true">
    <circle cx="23" cy="23" r="21" fill="#2d9be6" stroke="#fff" stroke-width="3"/>
    <path d="M18 13 L33 23 L18 33 Z" fill="#fff"/>
  </svg>
  <div class="hero-caption">
    <h2>LOREM IPSUM DOLOR SIT AMET</h2>
    <p>nuno valencia di maria eats deba</p>
  </div>
</section>

<svg class="water" width="813" height="60" viewBox="0 0 813 60" aria-hidden="true">
  <defs><linearGradient id="waterFill" x1="0" y1="0" x2="0" y2="1">
    <stop offset="0" stop-color="#2f86d0"/><stop offset="1" stop-color="#eef6fc" stop-opacity="0"/></linearGradient></defs>
  <path d="M0 14 Q20 8 40 13 T80 12 T120 14 T160 10 T200 14 T240 11 T280 14 T320 9 T360 13 T400 11 T440 14 T480 9 T520 13 T560 12 T600 14 T640 10 T680 13 T720 11 T760 14 T813 10 V60 H0 Z" fill="url(#waterFill)"/>
  <path d="M0 14 Q20 8 40 13 T80 12 T120 14 T160 10 T200 14 T240 11 T280 14 T320 9 T360 13 T400 11 T440 14 T480 9 T520 13 T560 12 T600 14 T640 10 T680 13 T720 11 T760 14 T813 10" fill="none" stroke="#fff" stroke-width="1.5" opacity=".85"/>
</svg>

<section class="features">
  <div class="feature" style="left:78px">
    <div class="feature-disc" role="img" aria-label="Photo of a hot tub shell" style="background:linear-gradient(180deg,#e9eef2 0,#c9d5de 30%,#3e5a78 55%,#2a3f58 75%,#d9e0e6 100%)"></div>
    <div class="feature-label">High-end<br>products</div>
  </div>
  <div class="feature" style="left:201px">
    <div class="feature-disc" role="img" aria-label="Picture of a money bag with stacked coins" style="background:linear-gradient(180deg,#f8efe0 0,#e8c48f 45%,#c98a3e 80%,#f3e2c4 100%)"></div>
    <div class="feature-label">Low monthly<br>maintenace</div>
  </div>
  <div class="feature" style="left:328px">
    <span class="feature-disc"><svg viewBox="0 0 96 96" aria-hidden="true">
      <rect width="96" height="96" fill="#f2e7cf"/>
      <rect x="45" y="18" width="6" height="6" fill="#bbb"/>
      <rect x="18" y="24" width="60" height="42" rx="2" fill="#161616"/>
      <rect x="22" y="28" width="52" height="34" fill="#2a2a2a"/>
      <rect x="45" y="66" width="6" height="8" fill="#bbb"/>
      <rect x="30" y="74" width="36" height="4" rx="2" fill="#999"/>
    </svg></span>
    <div class="feature-label">After<br>care &amp; training</div>
  </div>
  <div class="feature" style="left:456px">
    <span class="feature-disc"><svg viewBox="0 0 96 96" aria-hidden="true">
      <rect width="96" height="96" fill="#f7f7f7"/>
      <rect x="38" y="28" width="44" height="34" fill="#f7c600" stroke="#333" stroke-width="1.5"/>
      <path d="M14 62 V46 L22 36 H38 V62 Z" fill="#2f6fd0" stroke="#1a3f80" stroke-width="1.5"/>
      <path d="M20 46 L25 39 H33 V46 Z" fill="#cfe6fa"/>
      <rect x="12" y="60" width="72" height="6" fill="#555"/>
      <circle cx="26" cy="68" r="6" fill="#222"/><circle cx="26" cy="68" r="2.5" fill="#bbb"/>
      <circle cx="70" cy="68" r="6" fill="#222"/><circle cx="70" cy="68" r="2.5" fill="#bbb"/>
    </svg></span>
    <div class="feature-label">Free delivery<br>&amp; installation</div>
  </div>
  <div class="feature" style="left:579px">
    <div class="feature-disc" role="img" aria-label="Photo of a man relaxing in a hot tub" style="background:linear-gradient(180deg,#9aa39c 0,#b69479 40%,#8fb0bf 70%,#6f98ad 100%)"></div>
    <div class="feature-label">2 free<br>drains &amp; fills</div>
  </div>
  <div class="feature" style="left:702px">
    <span class="feature-disc"><svg viewBox="0 0 96 96" aria-hidden="true">
      <rect width="96" height="96" fill="#e9dbbd"/>
      <circle cx="48" cy="48" r="30" fill="#f5f8fb" stroke="#5f86b5" stroke-width="4"/>
      <circle cx="48" cy="48" r="24" fill="#eef2f6" stroke="#c7d3df" stroke-width="1"/>
      <path d="M34 44 A15 15 0 0 1 60 38" fill="none" stroke="#555" stroke-width="5"/>
      <path d="M56 32 L66 38 L56 44 Z" fill="#555"/>
      <path d="M62 52 A15 15 0 0 1 36 58" fill="none" stroke="#555" stroke-width="5"/>
      <path d="M40 52 L30 58 L40 64 Z" fill="#555"/>
    </svg></span>
    <div class="feature-label">30 exchange<br>guarantee</div>
  </div>
</section>

<div class="divider"></div>

<section class="cards">
  <article class="card" style="left:28px">
    <div class="card-photo" role="img" aria-label="Photo of a woman with a glass at a spa" style="background:linear-gradient(90deg,#7a5a34 0,#c4925f 30%,#e8c9a2 55%,#b98758 80%,#e6d0a8 100%)"><span>Hot Tub</span></div>
    <p>Lorem ipsum onsectetuer adipiscing elit, sed diam nonummy nibh euismod tincidunt ut laoreet dolore magna aliquam erat volutpat. Ut wisi enim ad minim veniam.</p>
    <a class="more-info" href="#">MORE INFO ····›</a>
  </article>
  <article class="card" style="left:216px">
    <div class="card-photo" role="img" aria-label="Photo of a woman resting among rose petals" style="background:linear-gradient(90deg,#b7464b 0,#d88b86 35%,#e3bca8 60%,#5a3a30 85%,#2e2220 100%)"><span>Hot Tub</span></div>
    <p>Lorem ipsum onsectetuer adipiscing elit, sed diam nonummy nibh euismod tincidunt ut laoreet dolore magna aliquam erat volutpat. Ut wisi enim ad minim veniam.</p>
    <a class="more-info" href="#">MORE INFO ····›</a>
  </article>
  <article class="card" style="left:403px">
    <div class="card-photo" role="img" aria-label="Photo of a man relaxing in a pool" style="background:linear-gradient(180deg,#4d86c8 0,#8ec4ec 40%,#c8e6f8 60%,#58a6e0 100%)"><span>Hot Tub</span></div>
    <p>Lorem ipsum onsectetuer adipiscing elit, sed diam nonummy nibh euismod tincidunt ut laoreet dolore magna aliquam erat volutpat. Ut wisi enim ad minim veniam.</p>
    <a class="more-info" href="#">MORE INFO ····›</a>
  </article>
  <article class="card" style="left:591px">
    <div class="card-photo" role="img" aria-label="Photo of a man receiving a spa massage" style="background:linear-gradient(90deg,#8c5228 0,#c98a55 35%,#e9b987 60%,#7a4a26 85%,#d6a070 100%)"><span>Hot Tub</span></div>
    <p>Lorem ipsum onsectetuer adipiscing elit, sed diam nonummy nibh euismod tincidunt ut laoreet dolore magna aliquam erat volutpat. Ut wisi enim ad minim veniam.</p>
    <a class="more-info" href="#">MORE INFO ····›</a>
  </article>
</section>

<footer class="site-footer">
  <div class="footer-col" style="left:0;width:176px;padding-left:45px">
    <h3>Quick Links</h3>
    <ul><li>Home</li><li>About Us</li><li>Services</li><li>Contact</li></ul>
  </div>
  <div class="footer-col" style="left:176px;width:173px;padding-left:60px">
    <h3>Products</h3>
    <ul><li>Hot Tub Model 1</li><li>Hot Tub Model 2</li><li>Hot Tub Model 3</li><li>Hot Tub Model 4</li></ul>
  </div>
  <div class="footer-col" style="left:349px;width:173px;padding-left:45px">
    <h3>Get In Touch</h3>
    <ul><li>Find us in Friendlane</li><li>Follow us in Chirpline</li><li>Find us in Worknet</li><li>Find us in Clipstream</li></ul>
  </div>
  <div class="footer-col contact" style="left:522px;width:291px;padding-left:32px">
    <h3>Contact Details</h3>
    <ul><li>742 Cedar Ridge Ave NE,</li><li>Albuquerque, NM 87112</li><li>Phone: (505) 555-0182</li><li>Email id: info@warmsoaksalbuquerque.example</li></ul>
  </div>
</footer>

<p class="copyright">© 2013, All Rights Reserved, warmsoaksalbuquerque.example</p>
</body>
</html>
```